Church Rivers of Morning Gospel Booklet Design

We need a booklet designed that we will be printing to hand out in our community. Wording for each page will be provided and we need graphic design to produce the layouts in a format ready for print. Booklet will be 4.75" x 4.75" square and a total of 12 pages: 1 cover page front, 1 cover page back, 10 inside pages some of which will be full spread across 2 pages.

Target Market(s)

English speaking Westerners

Industry/Entity Type

Religious

Font styles to use
Serif

Colors
ffffff
85abd2
0292cd
33b8a4
5c5c5c

Requirements
Must have
• Minimalist design with clean look described in attached document
Nice to have
• Aesthetically pleasing graphics, crisp fonts, excellent turn around times
Should not have
• Effeminate design, busy look with too much graphic and text

```html
<!DOCTYPE html>
<html lang="en">
<head>
<meta charset="utf-8">
<title>Rivers of Morning – Gospel Booklet Spreads</title>
<link href="https://fonts.googleapis.com/css2?family=Open+Sans:wght@300;400;600;700&family=Noto+Serif:wght@400;700&family=Oswald:wght@300;400;500&display=swap" rel="stylesheet">
<style>
:root{
  --backdrop:#bde6e3;
  --white:#ffffff;
  --sky:#85abd2;
  --azure:#0292cd;
  --teal:#33b8a4;
  --ink:#5c5c5c;
  --heading:#1a8fcf;
}
*{margin:0;padding:0;box-sizing:border-box}
html,body{width:768px;height:1200px;overflow:hidden}
body{background:var(--backdrop);position:relative;font-family:"Open Sans",Arial,sans-serif;color:var(--ink)}
.page,.spread{position:absolute;overflow:hidden;background:var(--white)}
.panel{position:absolute}
.photo{position:absolute}
.body-copy{font-size:4px;line-height:5.5px;text-align:justify}

/* Cover */
.cover{left:80px;top:94px;width:273px;height:272px;background:linear-gradient(180deg,#0a93d0 0%,#1aa5bf 55%,#2fb6a6 100%)}
.cover svg{position:absolute;left:0;top:0}
.cover-title{position:absolute;left:16px;top:140px;color:var(--white);line-height:1}
.cover-title .light{display:block;font-weight:300;font-size:23px;letter-spacing:.3px;text-transform:uppercase}
.cover-title .bold{display:block;font-family:"Noto Serif",Georgia,serif;font-weight:700;font-size:28px;margin-top:3px;text-transform:uppercase}

.cross-page{left:376px;top:82px;width:286px;height:286px;
  background:
    linear-gradient(180deg,rgba(255,255,255,0) 58%,rgba(170,168,160,.85) 78%,rgba(120,118,110,.9) 88%,rgba(215,214,210,.95) 100%),
    radial-gradient(circle at 78% 30%,#fffdf6 0%,#fff1dc 12%,#f9d9e6 30%,#efe4f1 48%,#fbf9fb 70%,#ffffff 100%)}

/* Spread 2 */
.spread-two{left:110px;top:441px;width:535px;height:267px}
.worship-photo{left:0;top:0;width:267px;height:267px;
  background:
    radial-gradient(ellipse 45% 30% at 45% 38%,rgba(255,246,225,.95) 0%,rgba(255,230,200,.4) 60%,rgba(255,230,200,0) 100%),
    linear-gradient(180deg,#eea48a 0%,#f4b98f 30%,#f6c79a 48%,#d9a08e 66%,#8e7fab 80%,#3a3247 90%,#1c1822 100%)}
.intro-text{left:267px;top:0;width:268px;height:106px;padding:24px 18px 0 44px}
.section-head{font-weight:600;color:var(--heading);text-transform:uppercase}
.intro-text .section-head{font-size:11px;line-height:13px;letter-spacing:.2px}
.intro-text .lede{font-family:"Noto Serif",Georgia,serif;font-size:8.3px;margin-top:1px;letter-spacing:.3px}
.intro-text .verse{font-size:6.6px;margin-top:10px;padding-left:6px;text-indent:-5px;line-height:9px}
.chapel-photo{left:267px;top:106px;width:268px;height:161px;
  background:
    radial-gradient(circle at 20% 25%,rgba(255,240,190,.9) 0%,rgba(255,240,190,0) 22%),
    radial-gradient(circle at 50% 18%,rgba(255,250,215,.8) 0%,rgba(255,250,215,0) 18%),
    linear-gradient(90deg,rgba(0,0,0,0) 45%,rgba(90,52,28,.85) 58%,rgba(90,52,28,.85) 70%,rgba(0,0,0,0) 74%),
    linear-gradient(180deg,#e3c078 0%,#c99549 45%,#b0753a 70%,#caa070 100%)}

/* Spread 3 */
.spread-three{left:39px;top:754px;width:330px;height:165px}
.truths{left:0;top:0;width:165px;height:110px;padding:15px 10px 0 11px}
.truths .section-head{font-size:6px;line-height:7.6px;font-weight:700;width:118px}
.truths ol{list-style:none;margin-top:6px}
.truths li{position:relative;padding-left:13px;font-size:3.7px;line-height:4.6px;height:17.5px}
.truths li svg{position:absolute;left:0;top:-1px}
.people-photo{left:0;top:110px;width:165px;height:55px;
  background:linear-gradient(90deg,#7c6c5e 0%,#b39c84 30%,#6d5a4d 55%,#a48c76 80%,#5b4b40 100%)}
.praise-photo{left:165px;top:0;width:70px;height:165px;
  background:linear-gradient(180deg,#ede2d3 0%,#d7bc9a 35%,#9a7458 65%,#3f312a 100%)}
.grave-text{left:235px;top:0;width:95px;height:108px;padding:34px 12px 0 12px}
.grave-text p+p{margin-top:4px}
.hill-photo{left:235px;top:108px;width:95px;height:57px;
  background:linear-gradient(180deg,#f5ead6 0%,#e7c48f 45%,#9a7344 72%,#1e1b16 88%,#14120f 100%)}

/* Spread 4 */
.spread-four{left:399px;top:754px;width:330px;height:165px}
.pews-photo{inset:0;
  background:
    linear-gradient(180deg,rgba(0,0,0,0) 60%,#8a5e2c 66%,#c08a45 74%,#7a4f24 82%,#b07d3e 90%,#5c3b1c 100%),
    linear-gradient(90deg,#6e7c84 0%,#8c8f88 40%,#a69a80 100%)}
.alienation{left:69px;top:0;width:96px;height:102px;background:var(--azure);color:var(--white);padding:26px 12px 0 14px}
.grace-text{left:165px;top:0;width:165px;height:102px;background:var(--white);padding:26px 12px 0 11px}
.grace-text .bullet{margin-top:9px;padding-left:5px}

/* Spread 5 */
.spread-five{left:46px;top:962px;width:330px;height:165px}
.family-photo{left:0;top:0;width:214px;height:165px;
  background:
    radial-gradient(ellipse 40% 30% at 35% 45%,rgba(235,200,160,.7) 0%,rgba(235,200,160,0) 100%),
    linear-gradient(180deg,#a26e42 0%,#7a4b2a 45%,#4a2d1c 62%,#1a1210 72%,#0e0a09 100%)}
.salvation-text{left:214px;top:0;width:116px;height:165px;padding:34px 19px 0 17px}
.salvation-text .bullet{margin-top:7px;padding-left:3px}

/* Spread 6 */
.spread-six{left:399px;top:962px;width:330px;height:165px}
.church-photo{left:0;top:0;width:165px;height:165px;
  background:
    radial-gradient(ellipse 35% 55% at 22% 50%,rgba(170,220,245,.7) 0%,rgba(170,220,245,0) 100%),
    linear-gradient(180deg,#0b9cd7 0%,#3cb1e2 45%,#1d8fca 75%,#0a76b4 100%)}
.growth-text{left:70px;top:13px;width:78px;color:var(--white)}
.sunset-photo{left:165px;top:0;width:165px;height:165px;
  background:
    radial-gradient(ellipse 30% 14% at 55% 70%,rgba(255,225,140,.95) 0%,rgba(255,170,70,.6) 50%,rgba(255,170,70,0) 100%),
    linear-gradient(180deg,#1b3a5a 0%,#2b4e6f 35%,#6b6a6c 55%,#d99548 68%,#8a5a34 80%,#3e2a1e 100%)}
.confession{left:165px;top:15px;width:165px;text-align:center;color:var(--white);font-family:"Oswald","Arial Narrow",sans-serif;text-transform:uppercase}
.confession .small{font-size:4.9px;font-weight:400;line-height:6.4px}
.confession .big{font-size:12px;font-weight:500;line-height:14px;margin:1px 0}
.confession .saved{font-size:13px;font-weight:300;line-height:15px;margin-top:2px}
</style>
</head>
<body>

<section class="page cover">
  <svg width="273" height="272" viewBox="0 0 273 272" aria-hidden="true">
    <path d="M18 134 V14 H255 V253 H18 V200" fill="none" stroke="#ffffff" stroke-width="3"/>
  </svg>
  <h1 class="cover-title"><span class="light">Rivers of</span><span class="bold">Morning</span></h1>
</section>

<section class="page cross-page" role="img" aria-label="Wooden cross on a rocky hilltop against a bright, glowing pastel sky"></section>

<section class="spread spread-two">
  <div class="photo worship-photo" role="img" aria-label="Silhouetted worshippers raising hands beneath a faint cross in a warm sunset sky"></div>
  <div class="panel intro-text">
    <h2 class="section-head">God willingly created the universe</h2>
    <p class="lede">meaning he envisioned, designed, and made us.</p>
    <p class="verse">• In the beginning God created the heavens and the earth. (Genesis 1:1)</p>
  </div>
  <div class="photo chapel-photo" role="img" aria-label="Wooden cross in front of a softly lit church aisle"></div>
</section>

<section class="spread spread-three">
  <div class="panel truths">
    <h2 class="section-head">This reality establishes some foundational truths for all of us:</h2>
    <ol>
      <li><svg width="9" height="9" viewBox="0 0 9 9"><circle cx="4.5" cy="4.5" r="4" fill="none" stroke="#0292cd" stroke-width=".6"/><text x="4.5" y="6.3" font-size="5" text-anchor="middle" fill="#0292cd" font-family="Open Sans">1</text></svg>God loves us – he didn't have to create us; we are here because he couldn't imagine life without us.</li>
      <li><svg width="9" height="9" viewBox="0 0 9 9"><circle cx="4.5" cy="4.5" r="4" fill="none" stroke="#0292cd" stroke-width=".6"/><text x="4.5" y="6.3" font-size="5" text-anchor="middle" fill="#0292cd" font-family="Open Sans">2</text></svg>God is the proper authority in our lives – if he designed and made us, he rightfully owns us.</li>
      <li><svg width="9" height="9" viewBox="0 0 9 9"><circle cx="4.5" cy="4.5" r="4" fill="none" stroke="#0292cd" stroke-width=".6"/><text x="4.5" y="6.3" font-size="5" text-anchor="middle" fill="#0292cd" font-family="Open Sans">3</text></svg>God knows the purpose of our lives – if he designed and made us, he knows why we are here.</li>
      <li><svg width="9" height="9" viewBox="0 0 9 9"><circle cx="4.5" cy="4.5" r="4" fill="none" stroke="#0292cd" stroke-width=".6"/><text x="4.5" y="6.3" font-size="5" text-anchor="middle" fill="#0292cd" font-family="Open Sans">4</text></svg>God's truth is the truth we need – if he designed and made us, he knows what it takes for life to go well for us.</li>
    </ol>
  </div>
  <div class="photo people-photo" role="img" aria-label="Congregation with arms raised in worship"></div>
  <div class="photo praise-photo" role="img" aria-label="Worshipper raising hands toward a bright window"></div>
  <div class="panel grave-text body-copy">
    <p>But we, mankind, have all rejected God's authority in our lives. And because he rightfully owns us, our rebellion against God is a grave injustice; an act of treason for which we deserve to be cut off from God forever.</p>
    <p>For the wages of sin is death… (Romans 6:23)</p>
  </div>
  <div class="photo hill-photo" role="img" aria-label="Cross silhouetted on a grassy hill at sunrise"></div>
</section>

<section class="spread spread-four">
  <div class="photo pews-photo" role="img" aria-label="Man seen from behind sitting in wooden church pews"></div>
  <div class="panel alienation body-copy">This alienation from God is evident in a myriad of ways including poverty, crime, conflict in our relationships, and our internal struggles. But worse, when we die, we must face the consequences for our rejection of God by spending eternity in hell – a lake of fire created by God as the place where our treason is brought to justice.</div>
  <div class="panel grace-text body-copy">
    <p>But God does not want you to pay for your own sins. God loves us so much he sent his only son to save us. Jesus Christ died on the cross to serve our sentence for our rebellion against God and rose again on the third day. Since Christ paid our full penalty, we can be completely forgiven and reconciled to God.</p>
    <p class="bullet">• For God so loved the world that he sent his one and only son that whosoever believes in him will not perish but have eternal life.</p>
  </div>
</section>

<section class="spread spread-five">
  <div class="photo family-photo" role="img" aria-label="Family reading the Bible together in a church pew"></div>
  <div class="panel salvation-text body-copy">
    <p>First, ask Jesus Christ to save you (Since he is God, he can hear you); Acknowledge that God is the rightful authority of the universe and your life. Apologize to him for your rebellion against God. Ask Jesus Christ to come into your life as your Lord and Savior. This decision will immediately trigger his miracle of salvation in you. God now lives in you!</p>
    <p class="bullet">• If you confess with your mouth that Jesus is Lord and believe in your heart that God raised him from the dead, you will be saved." (Romans 10:9)</p>
  </div>
</section>

<section class="spread spread-six">
  <div class="photo church-photo" role="img" aria-label="White church tower and palm trees in a blue duotone"></div>
  <p class="panel growth-text body-copy">Next, God has given us the Bible and his church as the key tools for us to grow in our understanding of God and our personal relationship with him. So, it is essential you find a local church that believes the Bible is 100% true. Tell one of the pastors you are a brand new Christian and they will help you from there.</p>
  <div class="photo sunset-photo" role="img" aria-label="Sun rising over mountain ridges beneath a deep blue sky"></div>
  <div class="panel confession">
    <p class="small">If you confess with your mouth,</p>
    <p class="big">“Jesus is Lord,”</p>
    <p class="small">and believe in your hwart that<br>God raised him from the dead</p>
    <p class="saved">You will be saved</p>
  </div>
</section>

</body>
</html>
```